Hacienda Valle Dorado Business cards

We would like 3 individual business cards with the logo you designed:

1) Marta Pellworth - Phone: 206 555 0147
2) Theodore K Pellworth - Phone 206 555 0183
3) Dana Whitlow - Phone 360-555-0126

Address for all three cards:
4217 288th Ave NE
Alder Hollow, OR 98019
HaciendaValleDorado@mailbox-example.com

```html
<!DOCTYPE html>
<html lang="en">
<head>
<meta charset="utf-8">
<title>Hacienda Valle Dorado – Business Card</title>
<link href="https://fonts.googleapis.com/css2?family=Cinzel:wght@400;700&family=Tinos&display=swap" rel="stylesheet">
<style>
  :root {
    --page: #ecebe8;
    --card-light: #ffffff;
    --card-dark: #000000;
    --ink: #111111;
    --ink-reverse: #ffffff;
    --shadow: rgba(0, 0, 0, 0.25);
  }
  * { box-sizing: border-box; margin: 0; padding: 0; }
  html, body {
    width: 1200px;
    height: 1000px;
    overflow: hidden;
    background: var(--page);
  }
  .canvas { position: relative; width: 1200px; height: 1000px; }

  .card {
    position: absolute;
    width: 640px;
    height: 360px;
    box-shadow: 0 10px 28px var(--shadow);
    overflow: hidden;
  }
  .card--front { left: 60px; top: 90px; background: var(--card-light); color: var(--ink); }
  .card--back  { left: 500px; top: 550px; background: var(--card-dark); color: var(--ink-reverse); }

  .brand {
    position: absolute;
    display: flex;
    flex-direction: column;
    align-items: center;
    gap: 14px;
  }
  .brand__mark {
    width: 90px;
    height: 90px;
    border-radius: 50%;
    background: currentColor;
  }
  .brand__name {
    font-family: "Cinzel", serif;
    font-weight: 400;
    font-size: 20px;
    letter-spacing: 0.5px;
    text-transform: uppercase;
    white-space: nowrap;
  }
  .card--front .brand { left: 20px; top: 50px; width: 310px; }
  .card--back .brand { left: 0; right: 0; top: 110px; }

  .holder {
    position: absolute;
    left: 20px;
    width: 310px;
    top: 250px;
    text-align: center;
    font-family: "Cinzel", serif;
    font-weight: 700;
    font-size: 22px;
    letter-spacing: 0.5px;
    text-transform: uppercase;
  }

  .contacts {
    position: absolute;
    left: 355px;
    right: 16px;
    top: 56px;
    list-style: none;
    font-family: "Tinos", serif;
    font-size: 12px;
    line-height: 1.35;
  }
  .contacts__item { display: flex; align-items: flex-start; gap: 6px; margin-bottom: 5px; }
  .contacts__icon { flex: none; width: 14px; height: 14px; margin-top: 1px; }
</style>
</head>
<body>
<main class="canvas">

  <section class="card card--front" aria-label="Business card front">
    <div class="brand">
      <span class="brand__mark" aria-hidden="true"></span>
      <span class="brand__name">Hacienda Valle Dorado</span>
    </div>
    <p class="holder">Dana Whitlow</p>
    <ul class="contacts">
      <li class="contacts__item">
        <svg class="contacts__icon" viewBox="0 0 14 14" aria-hidden="true"><circle cx="7" cy="7" r="7" fill="#111"/><path d="M4.6 3.6l1.4 1.5-.8 1c.5 1 1.2 1.7 2.2 2.2l1-.8 1.5 1.4-.9 1.3C6.8 10 4 7.2 3.4 4.5z" fill="#fff"/></svg>
        <span>360-555-0126</span>
      </li>
      <li class="contacts__item">
        <svg class="contacts__icon" viewBox="0 0 14 14" aria-hidden="true"><circle cx="7" cy="7" r="7" fill="#111"/><rect x="3.5" y="4.5" width="7" height="5" fill="none" stroke="#fff" stroke-width="0.9"/><path d="M3.5 4.5L7 7.3l3.5-2.8" fill="none" stroke="#fff" stroke-width="0.9"/></svg>
        <span>HaciendaValleDorado@mailbox-example.com</span>
      </li>
      <li class="contacts__item">
        <svg class="contacts__icon" viewBox="0 0 14 14" aria-hidden="true"><circle cx="7" cy="7" r="7" fill="#111"/><path d="M7 3a2.6 2.6 0 0 0-2.6 2.6C4.4 7.6 7 11 7 11s2.6-3.4 2.6-5.4A2.6 2.6 0 0 0 7 3z" fill="#fff"/><circle cx="7" cy="5.6" r="1" fill="#111"/></svg>
        <span>4217 288th Ave NE Alder Hollow,<br>OR 98019</span>
      </li>
    </ul>
  </section>

  <section class="card card--back" aria-label="Business card back">
    <div class="brand">
      <span class="brand__mark" aria-hidden="true"></span>
      <span class="brand__name">Hacienda Valle Dorado</span>
    </div>
  </section>

</main>
</body>
</html>
```